Hot young IT advisor needs business cards as upscale and innovative as they are

We need business cards that make a statement about who we are, as a young and upscale IT advisor. Our whole angle is innovation and tenacity in our personal relationships with our clients. We've just done a brand overhaul and need cards that have the new logos, but we're also looking for someone with a sixth sense who can capture what sets us apart and communicate that with a business card. Clean, minimalist, upscale, innovative, personal. Our budget only allows room for them to be soft-touch, no spot gloss or foil designs please.

Target Market(s)

High-level decision makers at middle-market and large organizations in the healthcare, financial services, sports and entertainment, K-12 education, college and university, state and local government, and federal government sectors.

Industry/Entity Type

Information Technology

Font styles to use
Sans Serif

Colors
ec1f27
606060
ffffff

Requirements
Should not have
• Designs with low contrast which would require spot-gloss or embossing.

```html
<!DOCTYPE html>
<html lang="en">
<head>
<meta charset="utf-8">
<title>Kelvora Business Card</title>
<link rel="stylesheet" href="https://fonts.googleapis.com/css2?family=Lato:wght@400;700&display=swap">
<style>
  :root {
    --red: #ec1f27;
    --grey: #606060;
    --ink: #2e2e2e;
    --white: #ffffff;
    --backdrop: #dcdcdc;
    --card-dark: #2f302e;
    --pattern-red: #7a1a22;
  }
  * { margin: 0; padding: 0; box-sizing: border-box; }
  html, body { width: 1200px; height: 900px; overflow: hidden; }
  body {
    background: var(--backdrop);
    font-family: "Lato", sans-serif;
    position: relative;
  }
  .card {
    position: absolute;
    width: 520px;
    height: 300px;
    border-radius: 26px;
    overflow: hidden;
  }
  .card-back {
    left: 90px;
    top: 130px;
    background: var(--card-dark);
  }
  .back-pattern {
    position: absolute;
    inset: 0;
    background: linear-gradient(135deg, var(--card-dark) 0%, var(--pattern-red) 50%, var(--card-dark) 100%);
    opacity: 0.55;
  }
  .back-brand {
    position: absolute;
    left: 0; right: 0; top: 50%;
    transform: translateY(-50%);
    text-align: center;
    color: var(--white);
    font-size: 30px;
    font-weight: 400;
    letter-spacing: 0.28em;
  }
  .card-front {
    left: 590px;
    top: 470px;
    background: var(--white);
    color: var(--ink);
  }
  .brand {
    position: absolute;
    left: 36px;
    top: 82px;
    font-size: 40px;
    font-weight: 400;
    letter-spacing: 0.26em;
    color: var(--ink);
  }
  .person {
    position: absolute;
    left: 36px;
    top: 158px;
  }
  .person-name {
    font-size: 18px;
    font-weight: 700;
    letter-spacing: 0.02em;
  }
  .person-name .surname { color: var(--red); font-weight: 400; }
  .person-title { font-size: 14px; color: var(--grey); margin-top: 1px; }
  .contacts {
    position: absolute;
    left: 36px;
    top: 212px;
    list-style: none;
    font-size: 14px;
    line-height: 21px;
    color: var(--ink);
  }
  .contacts li { display: flex; align-items: center; gap: 8px; }
  .contacts svg { width: 12px; height: 12px; fill: var(--red); flex: none; }
  .address {
    position: absolute;
    right: 30px;
    top: 150px;
    text-align: right;
    font-size: 14px;
    line-height: 19px;
    color: var(--ink);
  }
</style>
</head>
<body>
  <section class="card card-back">
    <div class="back-pattern" role="img" aria-label="Repeating dark grey and red geometric brand pattern"></div>
    <div class="back-brand">KELVORA</div>
  </section>

  <section class="card card-front">
    <div class="brand">KELVORA</div>

    <div class="person">
      <div class="person-name">MARCUS <span class="surname">HALE</span></div>
      <div class="person-title">Managing Director</div>
    </div>

    <ul class="contacts">
      <li>
        <svg viewBox="0 0 12 12" aria-hidden="true"><path d="M1 2.5C1 1.7 1.7 1 2.5 1h1l1 2.5-1.2 1a6 6 0 0 0 4.2 4.2l1-1.2L11 8.5v1c0 .8-.7 1.5-1.5 1.5C4.8 11 1 7.2 1 2.5z"/></svg>
        044-987 654 321
      </li>
      <li>
        <svg viewBox="0 0 12 12" aria-hidden="true"><path d="M1 2.5h10v7H1z M1.5 3l4.5 3.5L10.5 3" /></svg>
        hello@kelvora.com
      </li>
      <li>
        <svg viewBox="0 0 12 12" aria-hidden="true"><circle cx="6" cy="6" r="5"/></svg>
        www.kelvora.com
      </li>
    </ul>

    <div class="address">
      87 Ridgeway Lane<br>
      Northbrook, 60062
    </div>
  </section>
</body>
</html>
```